Book Cover Design Project - Pickup and Seduction Book Cover Needed

We are a small pickup and dating company based in Sydney, Australia called Copperfield Lantern Studio.
We have almost finished our first book that will be complete and printed in the very near future.
The title of the book will be:
"Quiet Harbour: Walking Calmly Through Mornings To Find Brighter Evenings"
With "Quiet Harbour" being the book title
and
"Walking Calmly Through Mornings To Find Brighter Evenings" being the tagline.
The book is about being honest, sincere and authentic when meeting and dating women and we require a book cover that makes a great first impression and excites guys while still being very classy and stylish.
We look forward to any and all submissions and we also look forward to choosing the best one from the submissions.
The book cover size is standard 6x9
The cover needs to be for epub AND printed books.
When designing this, design random blurb words. We will add this in later
Bleed for the book is atleast .125
The book is around 250 pages in size
The author''s name is Tobias Fenwright
Any other questions, please let me know
Reason: We want more submissions!

```html
<!DOCTYPE html>
<html lang="en">
<head>
<meta charset="utf-8">
<title>Quiet Harbour — Book Cover</title>
<link rel="stylesheet" href="https://fonts.googleapis.com/css2?family=Parisienne&family=Tinos&display=swap">
<style>
  :root {
    --page-bg: #ffffff;
    --wood-dark: #3b2d24;
    --wood-mid: #5a4738;
    --wood-light: #6e5a4a;
    --wood-seam: #2a1f18;
    --clay-pink: #c86a8e;
    --clay-violet: #a45a9c;
    --clay-coral: #e07a78;
    --heart-mist: rgba(255, 255, 255, 0.32);
    --title-ink: #ffffff;
    --tagline-ink: #f3eee9;
  }

  * { box-sizing: border-box; margin: 0; padding: 0; }

  html, body {
    width: 1200px;
    height: 900px;
    overflow: hidden;
    background: var(--page-bg);
  }

  .canvas {
    position: relative;
    width: 1200px;
    height: 900px;
    display: flex;
    align-items: center;
    justify-content: center;
  }

  .book-cover {
    position: relative;
    width: 533px;
    height: 800px;
    overflow: hidden;
  }

  .cover-backdrop {
    position: absolute;
    inset: 0;
    background:
      linear-gradient(90deg, transparent 0 47.6%, var(--wood-seam) 47.6% 48.6%, transparent 48.6% 100%),
      linear-gradient(90deg, var(--wood-dark) 0%, var(--wood-mid) 25%, var(--wood-light) 50%, var(--wood-mid) 78%, var(--wood-dark) 100%);
  }

  .heart-accent {
    position: absolute;
    border-radius: 45% 45% 50% 50%;
  }

  .heart-accent--mist-small  { left: 104px; top: 42px;  width: 92px;  height: 90px;  background: var(--heart-mist); }
  .heart-accent--mist-medium { left: 236px; top: 66px;  width: 128px; height: 124px; background: var(--heart-mist); }
  .heart-accent--mist-large  { left: 270px; top: 258px; width: 176px; height: 150px; background: var(--heart-mist); }
  .heart-accent--coral       { left: 446px; top: 115px; width: 74px;  height: 82px;  background: var(--clay-coral); opacity: 0.9; }

  .love-column {
    position: absolute;
    left: 28px;
    top: 136px;
    width: 148px;
    height: 560px;
    border-radius: 18px;
    background: linear-gradient(180deg, var(--clay-violet) 0%, var(--clay-pink) 20%, var(--clay-coral) 32%, var(--clay-coral) 48%, var(--clay-violet) 60%, var(--clay-pink) 80%, var(--clay-violet) 100%);
    opacity: 0.88;
  }

  .title-block {
    position: absolute;
    left: 170px;
    top: 395px;
    width: 350px;
    text-align: center;
    color: var(--title-ink);
  }

  .book-title {
    font-family: "Parisienne", cursive;
    font-weight: 400;
    font-size: 80px;
    line-height: 1.05;
  }

  .book-title span { display: block; }

  .book-tagline {
    margin: 26px auto 0;
    width: 270px;
    font-family: "Tinos", serif;
    font-weight: 400;
    font-size: 21px;
    line-height: 1.4;
    color: var(--tagline-ink);
  }
</style>
</head>
<body>
  <main class="canvas">
    <section class="book-cover">
      <div class="cover-backdrop" role="img" aria-label="Weathered dark wooden planks joined by a vertical seam"></div>
      <div class="heart-accent heart-accent--mist-small" role="img" aria-label="Small translucent white heart"></div>
      <div class="heart-accent heart-accent--mist-medium" role="img" aria-label="Translucent white heart"></div>
      <div class="heart-accent heart-accent--mist-large" role="img" aria-label="Large translucent white heart"></div>
      <div class="heart-accent heart-accent--coral" role="img" aria-label="Small coral clay heart, slightly tilted"></div>
      <div class="love-column" role="img" aria-label="Handmade pink and violet clay letters spelling LOVE, with a coral clay heart in place of the O, stacked vertically"></div>
      <div class="title-block">
        <h1 class="book-title"><span>Quiet</span><span>Harbour</span></h1>
        <p class="book-tagline">Walking Calmly Through Mornings To Find Brighter Evenings</p>
      </div>
    </section>
  </main>
</body>
</html>
```